New Business Card for Web Design/Internet Marketing Company

Looking for a great looking new business card. We are a 10 year old web design, internet marketing and website management company that works mostly with small businesses.

Our new card needs to better match the colors and style of our website, be bold, extremely usable and slightly edgy.

Target Market(s)

Small/Medium businesses that have websites

Industry/Entity Type

Internet

Requirements
Must have
• Front and back design, full color, rounded corners please

Must use the colors/style of our website (JPG provided)

INFO FOR CARDS (as readable as possible please)
Mark Pellow
President/CEO
mark@brightlanesites.com
Phone: 520-481-7093
Toll Free: 866-481-7093
Address: 4315 E. Kestrel Ave. Ste. 140, Tucson, AZ 85733

THINGS I WANT TO PROMOTE (if there is room):
1. Our Website - www.brightlanesites.com

2. Social Media
Twitter: @brightlanesites
Facebook: www.socialpage.net/brightlanesites

3. Our Services
Web Design
Internet Marketing
Website Management

```html
<!DOCTYPE html>
<html lang="en">
<head>
<meta charset="utf-8">
<title>Bright Lane Sites – Business Card</title>
<link rel="stylesheet" href="https://fonts.googleapis.com/css2?family=Open+Sans:wght@300;400;600;700&display=swap">
<style>
  :root {
    --stage: #1d1d1d;
    --blue-deep: #0a67ab;
    --blue-light: #43b6da;
    --orange: #e08a1e;
    --ink-blue: #1f86bf;
    --ink-grey: #5a5a5a;
    --rule: #8a8a8a;
    --white: #ffffff;
  }
  * { box-sizing: border-box; margin: 0; padding: 0; }
  html, body { width: 1200px; height: 900px; overflow: hidden; }
  body {
    background: var(--stage);
    font-family: "Open Sans", Arial, sans-serif;
    position: relative;
  }
  .card {
    position: absolute;
    width: 632px;
    height: 361px;
    border-radius: 27px;
    overflow: hidden;
    box-shadow: 0 6px 18px rgba(0,0,0,.55);
  }
  /* front */
  .card-front {
    left: 264px; top: 88px;
    background: linear-gradient(160deg, var(--blue-deep) 20%, #1a86c2 60%, var(--blue-light) 100%);
    color: var(--white);
  }
  .services-title {
    position: absolute; left: 32px; top: 34px;
    color: var(--orange); font-weight: 600; font-size: 24px;
  }
  .service-list {
    position: absolute; left: 32px; top: 72px;
    list-style: none; font-size: 19px; line-height: 24px;
  }
  .service-list li::before {
    content: ""; display: inline-block;
    width: 14px; height: 8px; margin-right: 6px;
    border-top: 2px solid var(--orange); border-radius: 50%;
    transform: rotate(-15deg); vertical-align: middle;
  }
  .social {
    position: absolute; left: 32px; top: 168px;
    list-style: none; font-size: 19px; line-height: 28px;
    white-space: nowrap;
  }
  .social .mark {
    display: inline-block; width: 16px; height: 16px;
    background: var(--orange); border-radius: 3px;
    margin-right: 9px; vertical-align: -2px;
  }
  .site-link {
    position: absolute; left: 32px; top: 241px;
    color: var(--orange); font-size: 19px;
  }
  .front-brand {
    position: absolute; right: 30px; bottom: 18px;
    font-size: 42px; font-weight: 700; color: var(--white);
    letter-spacing: .5px; white-space: nowrap;
  }
  /* back */
  .card-back {
    left: 266px; top: 467px;
    background: var(--white);
  }
  .back-brand {
    position: absolute; left: 20px; top: 160px; width: 280px;
    text-align: center; white-space: nowrap;
    font-size: 25px; font-weight: 700; color: var(--ink-blue);
  }
  .back-brand .dot {
    display: inline-block; width: 16px; height: 16px;
    border-radius: 50%; background: var(--orange);
    margin-right: 8px; vertical-align: 1px;
  }
  .divider {
    position: absolute; left: 318px; top: 55px;
    width: 2px; height: 230px; background: var(--rule);
  }
  .contact { position: absolute; left: 367px; top: 64px; color: var(--ink-grey); white-space: nowrap; }
  .contact .name {
    color: var(--ink-blue); font-size: 24px; font-weight: 600;
    letter-spacing: 1.5px; line-height: 30px;
  }
  .contact .role { font-size: 16px; font-weight: 300; line-height: 20px; }
  .contact .address {
    margin-top: 44px; font-size: 16px; font-weight: 300; line-height: 21px;
    font-style: normal;
  }
  .contact .lines { margin-top: 12px; font-size: 16px; font-weight: 300; line-height: 23px; }
  .contact .label { color: var(--ink-blue); font-weight: 400; }
  .band { position: absolute; left: 0; bottom: 0; width: 632px; height: 27px; }
</style>
</head>
<body>
  <section class="card card-front">
    <h2 class="services-title">Our Service</h2>
    <ul class="service-list">
      <li>Web Design</li>
      <li>Internet Marketing</li>
      <li>Website Management</li>
    </ul>
    <ul class="social">
      <li><span class="mark"></span>@brightlanesites</li>
      <li><span class="mark"></span>www.socialpage.net/brightlanesites</li>
    </ul>
    <p class="site-link">www.brightlanesites.com</p>
    <p class="front-brand">Bright Lane Sites</p>
  </section>

  <section class="card card-back">
    <p class="back-brand"><span class="dot"></span>Bright Lane Sites</p>
    <div class="divider"></div>
    <div class="contact">
      <p class="name">Mark Pellow</p>
      <p class="role">President/CEO</p>
      <address class="address">4315 E. Kestrel Ave.<br>Ste. 140, Tucson, AZ 85733</address>
      <p class="lines">
        <span class="label">Phone.</span> 520-481-7093<br>
        <span class="label">Toll Free.</span> 866-481-7093<br>
        <span class="label">Email.</span> mark@brightlanesites.com
      </p>
    </div>
    <svg class="band" viewBox="0 0 632 27" aria-hidden="true">
      <defs>
        <linearGradient id="bandBlue" x1="0" x2="1" y1="0" y2="0">
          <stop offset="0" stop-color="#4bbbe0"/>
          <stop offset="1" stop-color="#0b6db1"/>
        </linearGradient>
      </defs>
      <polygon points="0,0 436,0 423,27 0,27" fill="#e08a1e"/>
      <polygon points="443,0 632,0 632,27 430,27" fill="url(#bandBlue)"/>
    </svg>
  </section>
</body>
</html>
```